Maravel - Refresh the look and feel of an existing website

We currently have an existing website www.maravelpartnersgroup.example however it needs a more refreshed 'look and feel'. We are a professional consultancy that works with large corporate organisations and government. Our 'tag line' is A New Way of Thinking. We want the site to communicate "Innovation" and Leading Edge Thinking.

Target Market(s)

Corporate and Professional Clients - Organisation and Business Change

Industry/Entity Type

Management Consulting

Number of Pages Required

1 page

Font styles to use
Sans Serif

Requirements
Must have
• Must have a professional Corporate look and feel. Header 'imagery' is ok but boxes on front page need changing ... along with the words. The focus on home page needs to 'call out' 3 main consulting areas:-
• - Change & Transformation Specialists
• - Innovative Solutions
• - Digital Transformation
• Tag Line for business is ... A New Way of Thinking (Highlighting Maravel as 'Thought Leaders' in business)
Nice to have
• Less "words' more imagery. Possibly an area for a 'video' or recent articles/blogs on the front page. Needs to have more of an 'interactive' feel. We are open to suggestions.
Should not have
• NA

```html
<!DOCTYPE html>
<html lang="en">
<head>
<meta charset="utf-8">
<title>Maravel Global Solutions</title>
<link rel="stylesheet" href="https://fonts.googleapis.com/css2?family=Open+Sans:wght@400;600;700&family=Oswald:wght@200;300;500&display=swap">
<style>
:root{
  --navy:#243d5c;
  --ink:#2a3a52;
  --accent:#36b5d8;
  --grey-bg:#efefef;
  --text:#555c66;
  --white:#ffffff;
}
*{margin:0;padding:0;box-sizing:border-box}
html,body{width:1200px;height:4045px;overflow:hidden}
body{position:relative;background:var(--white);font-family:"Open Sans",Arial,sans-serif;color:var(--text)}
.abs{position:absolute}
.photo{position:absolute}

/* header */
.hero{left:0;top:0;width:1200px;height:710px;background:
  radial-gradient(ellipse 260px 300px at 560px 420px,rgba(240,170,160,.85),rgba(240,170,160,0) 70%),
  radial-gradient(ellipse 380px 420px at 980px 360px,rgba(70,90,115,.75),rgba(70,90,115,0) 75%),
  radial-gradient(ellipse 300px 260px at 160px 520px,rgba(120,140,160,.8),rgba(120,140,160,0) 75%),
  linear-gradient(180deg,#dfe5ea 0%,#b9c6d2 30%,#8fa3b8 70%,#6d8399 100%)}
.hero-veil{left:0;top:0;width:1200px;height:710px;background:linear-gradient(180deg,rgba(255,255,255,.55) 0,rgba(255,255,255,0) 110px)}
.brand{display:flex;align-items:center;gap:14px}
.brand-dot{width:52px;height:52px;border-radius:50%;background:var(--navy)}
.brand-name{font-family:"Open Sans",sans-serif;font-weight:700;font-size:30px;letter-spacing:2px;color:var(--navy);line-height:1}
.brand-name small{display:block;font-size:12px;letter-spacing:2.5px;font-weight:700;margin-top:3px}
.site-brand{left:75px;top:26px}
.main-nav{right:62px;top:42px;display:flex;gap:30px;font-family:"Oswald",sans-serif;font-weight:300;font-size:17px;color:var(--ink);text-transform:uppercase}
.tagline{font-family:"Oswald",sans-serif;font-weight:200;text-transform:uppercase;line-height:1}
.tag-a{left:362px;top:150px;font-size:150px;color:var(--ink)}
.tag-new{left:238px;top:255px;font-size:200px;color:var(--ink);letter-spacing:-2px}
.tag-way{left:440px;top:350px;font-size:180px;color:var(--white)}
.tag-thinking{left:462px;top:498px;font-size:88px;color:var(--white);letter-spacing:1px}
.btn{display:inline-block;border:2px solid var(--accent);border-radius:22px;color:var(--accent);font-family:"Open Sans",sans-serif;font-weight:600;font-size:12px;letter-spacing:1px;text-transform:uppercase;text-align:center}
.hero-btn{left:476px;top:603px;width:168px;height:40px;line-height:36px;border-color:var(--ink);color:var(--ink);background:rgba(255,255,255,.35)}

/* team band */
.team-photo{left:0;top:809px;width:1200px;height:480px;background:
  radial-gradient(ellipse 420px 200px at 760px 420px,rgba(30,34,42,.85),rgba(30,34,42,0) 80%),
  radial-gradient(ellipse 140px 120px at 860px 210px,rgba(200,150,120,.7),rgba(200,150,120,0) 80%),
  radial-gradient(ellipse 200px 260px at 1140px 150px,rgba(110,150,80,.75),rgba(110,150,80,0) 80%),
  linear-gradient(90deg,#d9d2c8 0%,#c6c0b8 45%,#d4d8d2 80%,#b9c6a8 100%)}
.team-frame{left:113px;top:769px;width:502px;height:566px;border:6px solid var(--navy)}
.team-card{left:75px;top:825px;width:451px;height:443px;background:rgba(36,61,92,.94);padding:84px 42px 0 36px;color:var(--white)}
.team-card .brand-dot{background:var(--white);width:76px;height:76px}
.team-card .brand-name{color:var(--white);font-size:38px}
.team-card .brand-name small{font-size:15px}
.team-card h3{font-size:16px;font-weight:700;margin-top:26px}
.team-card p{font-size:14px;line-height:1.55;margin-top:14px}
.team-card .btn{margin-top:34px;width:152px;height:42px;line-height:38px}

/* services */
.wedge{left:0;top:1340px}
.svc-title{font-family:"Open Sans",sans-serif;font-weight:700;font-size:31px;line-height:1.05;color:var(--ink);text-transform:uppercase;letter-spacing:.5px}
.svc-rule{width:48px;height:2px;background:#9aa3ad}
.svc-text{font-size:13.5px;line-height:1.75;color:var(--text)}
.svc-btn{width:150px;height:42px;line-height:38px;background:var(--white)}
.video{left:631px;top:1367px;width:421px;height:251px;background:
  radial-gradient(ellipse 120px 90px at 300px 190px,rgba(210,215,220,.55),rgba(210,215,220,0) 80%),
  radial-gradient(ellipse 90px 70px at 390px 200px,rgba(90,140,80,.6),rgba(90,140,80,0) 80%),
  linear-gradient(160deg,#1f2a33 0%,#3e4b55 55%,#56636c 100%)}
.video h3{position:absolute;left:32px;top:38px;font-size:23px;font-weight:700;color:var(--white);text-transform:uppercase}
.video .play{position:absolute;left:32px;top:94px;display:flex;align-items:center;gap:14px;color:var(--white);font-style:italic;font-size:15px}
.video .btn{position:absolute;left:32px;top:168px;width:150px;height:42px;line-height:38px;border-color:var(--white);color:var(--white)}

.quote{left:615px;top:2543px;width:510px;height:459px;background:var(--navy);color:var(--white)}
.quote h3{position:absolute;left:60px;top:150px;font-size:23px;font-weight:700;text-transform:uppercase}
.quote .svc-rule{position:absolute;left:60px;top:213px;background:#8aa0b8}
.quote p{position:absolute;left:130px;top:200px;width:320px;font-size:13.5px;line-height:1.75;color:#d6dee8}
.quote .who{position:absolute;left:130px;top:350px;font-size:13.5px;font-weight:700}
.dots{position:absolute;left:130px;top:380px;display:flex;gap:6px}
.dots i{width:10px;height:10px;border-radius:50%;background:#8aa0b8}
.dots i:first-child{background:var(--white)}

/* blog */
.blog-head{left:73px;top:3083px}
.blog-head h2{font-size:22px;font-weight:700;color:#222;text-transform:uppercase}
.blog-head p{font-size:15px;color:#444;margin-top:6px}
.post{top:3190px;width:334px;height:424px;background:#efefef}
.post .photo{left:0;top:0;width:334px;height:262px}
.post .date{position:absolute;left:18px;top:280px;font-size:13px;color:#333}
.post h4{position:absolute;left:18px;top:306px;width:300px;font-size:15px;font-weight:700;color:#222;line-height:1.2}
.post p{position:absolute;left:18px;top:356px;width:300px;font-size:12.5px;line-height:1.6;color:#666}

/* footer */
.footer{left:0;top:3690px;width:1200px;height:355px;background:var(--navy);color:#c8d3df}
.f-col{top:38px;font-size:13px;line-height:1.9}
.f-col h5{font-size:15px;font-weight:700;color:var(--white);text-transform:uppercase;margin-bottom:16px}
.f-col b{color:var(--white);font-weight:700}
.f-input{width:196px;height:34px;border-radius:17px;background:var(--white);color:#999;font-size:12px;padding:8px 16px;margin-top:14px}
.f-go{position:absolute;left:206px;top:100px;width:34px;height:34px;border-radius:50%;border:2px solid var(--accent)}
.f-bar{left:0;top:274px;width:1200px;height:1px;background:#3d5777}
.f-brand{left:73px;top:298px;gap:10px}
.f-brand .brand-dot{width:32px;height:32px;background:var(--white)}
.f-brand .brand-name{font-size:16px;letter-spacing:1.5px;color:var(--white)}
.f-brand .brand-name small{font-size:7px;letter-spacing:1.5px}
.copy{left:248px;top:306px;font-size:13px}
.socials{right:75px;top:298px;display:flex;gap:8px}
.socials i{width:34px;height:34px;border-radius:50%;border:2px solid #c8d3df}
</style>
</head>
<body>

<header>
  <div class="abs hero" role="img" aria-label="Photo of business people meeting in a bright glass-walled office"></div>
  <div class="abs hero-veil"></div>
  <div class="abs brand site-brand"><span class="brand-dot"></span><span class="brand-name">MARAVEL<small>GLOBAL SOLUTIONS</small></span></div>
  <nav class="abs main-nav"><span>Home</span><span>About Us</span><span>Our Services</span><span>Solutions</span><span>What's Happening</span><span>Contact Us</span></nav>
  <div class="abs tagline tag-a">A</div>
  <div class="abs tagline tag-new">New</div>
  <div class="abs tagline tag-way">Way</div>
  <div class="abs tagline tag-thinking">of Thinking</div>
  <span class="abs btn hero-btn">Learn More</span>
</header>

<section>
  <div class="abs team-photo" role="img" aria-label="Photo of a smiling team of business professionals"></div>
  <div class="abs team-frame"></div>
  <div class="abs team-card">
    <div class="brand"><span class="brand-dot"></span><span class="brand-name">MARAVEL<small>GLOBAL SOLUTIONS</small></span></div>
    <h3>Lorem ipsum copy in and languages for layouts.</h3>
    <p>Our strength is our people - highly skilled, dedicated specialists who have proven experience delivering the outcomes that our clients need.</p>
    <span class="btn">Learn More</span>
  </div>
</section>

<section>
  <svg class="abs wedge" width="1200" height="1740" viewBox="0 0 1200 1740"><polygon points="0,0 1200,790 0,1735" fill="#efefef"/></svg>

  <div class="photo" style="left:119px;top:1408px;width:420px;height:421px;background:radial-gradient(ellipse 110px 190px at 130px 180px,rgba(45,55,70,.85),rgba(45,55,70,0) 80%),radial-gradient(ellipse 90px 160px at 310px 200px,rgba(230,225,215,.9),rgba(230,225,215,0) 80%),linear-gradient(180deg,#b8d0e2 0%,#dfe8ee 60%,#f3f4f4 88%,#ffffff 100%)" role="img" aria-label="Photo of two colleagues talking in an office"></div>
  <div class="abs svc-title" style="left:138px;top:1778px">Change &amp;<br>Transformation<br>Specialists</div>
  <div class="abs svc-rule" style="left:140px;top:1893px"></div>
  <p class="abs svc-text" style="left:202px;top:1882px;width:330px">Lorem ipsum dolor sit amet, consectetur adipiscing elit, sed do eiusmod tempor incididunt ut labore et dolore magna aliqua. Ut enim ad minim veniam, quis nostrud exercitation ullamco laboris nisi ut aliquip ex ea commodo.</p>
  <span class="abs btn svc-btn" style="left:202px;top:2017px">Learn More</span>

  <div class="abs video" role="img" aria-label="Video still of a team working at laptops">
    <h3>Watch Our Video</h3>
    <div class="play"><svg width="44" height="44" viewBox="0 0 44 44"><circle cx="22" cy="22" r="20" fill="none" stroke="#fff" stroke-width="2"/><polygon points="17,13 31,22 17,31" fill="#fff"/></svg>Play</div>
    <span class="btn">Learn More</span>
  </div>

  <div class="photo" style="left:631px;top:1688px;width:421px;height:416px;background:radial-gradient(ellipse 170px 110px at 210px 240px,rgba(80,150,190,.75),rgba(80,150,190,0) 80%),radial-gradient(ellipse 160px 220px at 210px 160px,rgba(50,56,64,.8),rgba(50,56,64,0) 80%),linear-gradient(180deg,#e6e8ea 0%,#c4c9ce 45%,#dde0e3 80%,#f2f3f4 100%)" role="img" aria-label="Photo of a businessman holding a glowing digital world map"></div>
  <div class="abs svc-title" style="left:648px;top:2058px">Digital<br>Transformation</div>
  <div class="abs svc-rule" style="left:650px;top:2148px"></div>
  <p class="abs svc-text" style="left:715px;top:2136px;width:330px">Lorem ipsum dolor sit amet, consectetur adipiscing elit, sed do eiusmod tempor incididunt ut labore et dolore magna aliqua. Ut enim ad minim veniam, quis nostrud exercitation ullamco laboris nisi ut aliquip ex ea commodo.</p>
  <span class="abs btn svc-btn" style="left:715px;top:2271px">Learn More</span>

  <div class="photo" style="left:119px;top:2117px;width:420px;height:418px;background:radial-gradient(ellipse 40px 90px at 215px 110px,rgba(200,60,55,.55),rgba(200,60,55,0) 80%),radial-gradient(ellipse 70px 130px at 230px 300px,rgba(250,250,250,.95),rgba(250,250,250,0) 80%),radial-gradient(ellipse 200px 120px at 210px 300px,rgba(140,140,140,.45),rgba(140,140,140,0) 80%),linear-gradient(180deg,#d8d8d6 0%,#e9e9e7 60%,#f4f4f3 100%)" role="img" aria-label="Photo of a thoughtful businesswoman beneath sketched rocket and idea drawings"></div>
  <div class="abs svc-title" style="left:138px;top:2485px">Innovative<br>Solutions</div>
  <div class="abs svc-rule" style="left:140px;top:2570px"></div>
  <p class="abs svc-text" style="left:202px;top:2559px;width:330px">Lorem ipsum dolor sit amet, consectetur adipiscing elit, sed do eiusmod tempor incididunt ut labore et dolore magna aliqua. Ut enim ad minim veniam, quis nostrud exercitation ullamco laboris nisi ut aliquip ex ea commodo.</p>
  <span class="abs btn svc-btn" style="left:202px;top:2697px">Learn More</span>

  <div class="abs quote">
    <h3>Why Client Love Us?</h3>
    <div class="svc-rule"></div>
    <p>Lorem ipsum dolor sit amet, consectetur adipiscing elit, sed do eiusmod tempor incididunt ut labore et dolore magna aliqua. Ut enim ad minim veniam, quis nostrud exercitation ullamco laboris nisi ut aliquip ex ea commodo.</p>
    <div class="who">Daniel Harper</div>
    <div class="dots"><i></i><i></i><i></i><i></i><i></i></div>
  </div>
</section>

<section>
  <div class="abs blog-head"><h2>Blog Posts</h2><p>Lorem ipsum copy in various charsets and languages for layouts.</p></div>

  <article class="abs post" style="left:73px">
    <div class="photo" style="background:radial-gradient(ellipse 90px 110px at 230px 160px,rgba(120,95,85,.7),rgba(120,95,85,0) 80%),radial-gradient(ellipse 80px 90px at 80px 140px,rgba(90,110,140,.7),rgba(90,110,140,0) 80%),linear-gradient(180deg,#f2f2f2 0%,#dcdfe2 60%,#b9bec3 100%)" role="img" aria-label="Photo of two colleagues reviewing a tablet"></div>
    <span class="date">January 27, 2016</span>
    <h4>Lorem ipsum dolor sit amet, consectetur adipiscing elit</h4>
    <p>sed do eiusmod tempor incididunt ut labore et dolore magna aliqua. Ut enim ad minim veniam, quis nostrud exercitation.</p>
  </article>
  <article class="abs post" style="left:434px">
    <div class="photo" style="background:radial-gradient(ellipse 110px 70px at 160px 190px,rgba(210,215,220,.75),rgba(210,215,220,0) 80%),radial-gradient(ellipse 80px 100px at 260px 110px,rgba(180,140,115,.6),rgba(180,140,115,0) 80%),linear-gradient(160deg,#2a323a 0%,#4a545e 55%,#6c7680 100%)" role="img" aria-label="Photo of a team meeting around laptops"></div>
    <span class="date">January 24, 2016</span>
    <h4>Lorem ipsum dolor sit amet, consectetur adipiscing elit</h4>
    <p>sed do eiusmod tempor incididunt ut labore et dolore magna aliqua. Ut enim ad minim veniam, quis nostrud exercitation.</p>
  </article>
  <article class="abs post" style="left:793px">
    <div class="photo" style="background:radial-gradient(ellipse 120px 150px at 110px 170px,rgba(35,42,55,.8),rgba(35,42,55,0) 80%),radial-gradient(ellipse 110px 140px at 260px 170px,rgba(45,55,72,.75),rgba(45,55,72,0) 80%),linear-gradient(180deg,#d6e0ea 0%,#b4c3d2 55%,#8a9aab 100%)" role="img" aria-label="Photo of two businessmen discussing documents"></div>
    <span class="date">November 3, 2015</span>
    <h4>Lorem ipsum dolor sit amet, consectetur adipiscing elit</h4>
    <p>sed do eiusmod tempor incididunt ut labore et dolore magna aliqua. Ut enim ad minim veniam, quis nostrud exercitation.</p>
  </article>
</section>

<footer class="abs footer">
  <div class="abs f-col" style="left:73px"><h5>About Us</h5>Our Team<br>Our Values<br>Giving Back</div>
  <div class="abs f-col" style="left:345px"><h5>Our Services</h5>Strategy and Design<br>Transformation<br>Change &amp; Culture<br>Organisational Development<br>Project Management<br>Organisational Efficiency<br>Specialist Placements</div>
  <div class="abs f-col" style="left:612px"><h5>Get In Touch</h5><b>AUS</b><br>1300 555 018 (AUS)<br><b>NZ</b><br>0800 555 204 (NZ)<br><b>INTL</b><br>1300 555 018<br>
    <span style="display:inline-flex;align-items:center;gap:8px"><svg width="16" height="12" viewBox="0 0 16 12"><rect x="0.5" y="0.5" width="15" height="11" fill="none" stroke="#c8d3df"/><polyline points="1,1 8,7 15,1" fill="none" stroke="#c8d3df"/></svg>info@maravelpartnersgroup.example</span></div>
  <div class="abs f-col" style="left:885px"><h5>Stay Informed</h5>Get news, views, insight and events<div class="f-input">Enter email address</div>
    <svg class="f-go" viewBox="0 0 34 34"><polyline points="13,10 20,17 13,24" fill="none" stroke="#36b5d8" stroke-width="2.5"/></svg></div>
  <div class="abs f-bar"></div>
  <div class="abs brand f-brand"><span class="brand-dot"></span><span class="brand-name">MARAVEL<small>GLOBAL SOLUTIONS</small></span></div>
  <div class="abs copy">Copyright © 2016 Maravel Global Solutions</div>
  <div class="abs socials"><i></i><i></i><i></i><i></i></div>
</footer>

</body>
</html>
```